Fernly Garage Doors Business Card

I need a Business Card for my garage door business:
Fernly Garage Doors.
please add:
logo
phone number: 833-2-FERNLY
(337-659)

email: service@fernlygaragedoors.com
website: www.fernlygaragedoors.com

The attached image is recommendation ONLY.

```html
<!DOCTYPE html>
<html lang="en">
<head>
<meta charset="utf-8">
<title>Fernly Garage Doors Business Card</title>
<link href="https://fonts.googleapis.com/css2?family=Open+Sans:wght@400;600;700&display=swap" rel="stylesheet">
<style>
  :root {
    --page-bg: #ecebe8;
    --card-teal: #4fc1cf;
    --card-white: #f7f7f5;
    --ink: #1c1c1c;
    --brand-teal: #4cc0cd;
    --shadow: rgba(0, 0, 0, 0.18);
  }
  html, body {
    margin: 0;
    padding: 0;
    width: 1200px;
    height: 900px;
    overflow: hidden;
    background: var(--page-bg);
    font-family: "Open Sans", sans-serif;
    color: var(--ink);
  }
  .canvas {
    position: relative;
    width: 1200px;
    height: 900px;
  }
  .card {
    position: absolute;
    box-shadow: 0 6px 18px var(--shadow);
  }
  .card-front {
    left: 238px;
    top: 62px;
    width: 555px;
    height: 343px;
    background: var(--card-teal);
  }
  .card-back {
    left: 457px;
    top: 518px;
    width: 560px;
    height: 344px;
    background: var(--card-white);
  }
  .holder {
    position: absolute;
    left: 32px;
    top: 107px;
  }
  .holder-name {
    margin: 0;
    font-size: 18px;
    font-weight: 700;
    line-height: 24px;
  }
  .holder-title {
    margin: 0;
    font-size: 14px;
    font-weight: 400;
    line-height: 18px;
  }
  .contact-list {
    list-style: none;
    margin: 26px 0 0;
    padding: 0;
    font-size: 14px;
    line-height: 20px;
  }
  .contact-item {
    display: flex;
    align-items: center;
    gap: 8px;
  }
  .contact-icon {
    width: 12px;
    height: 12px;
    flex: none;
  }
  .front-brand {
    position: absolute;
    left: 336px;
    top: 128px;
    width: 145px;
    display: flex;
    flex-direction: column;
    align-items: center;
    gap: 10px;
  }
  .brand-square {
    width: 54px;
    height: 54px;
    background: var(--ink);
  }
  .front-brand .brand-name {
    font-size: 17px;
    font-weight: 600;
    text-align: center;
    line-height: 21px;
  }
  .back-brand {
    position: absolute;
    left: 104px;
    top: 124px;
    display: flex;
    align-items: center;
    gap: 24px;
  }
  .back-brand .brand-square {
    width: 92px;
    height: 92px;
    background: var(--brand-teal);
  }
  .back-brand .brand-name {
    font-size: 30px;
    font-weight: 600;
    line-height: 36px;
    color: var(--ink);
  }
</style>
</head>
<body>
<main class="canvas">
  <section class="card card-front">
    <div class="holder">
      <p class="holder-name">Marcus Hale</p>
      <p class="holder-title">Managing Director</p>
      <ul class="contact-list">
        <li class="contact-item">
          <svg class="contact-icon" viewBox="0 0 12 12" aria-hidden="true"><path d="M2.5 1 L4.5 1 L5.3 3.4 L4 4.4 C4.6 5.8 6.2 7.4 7.6 8 L8.6 6.7 L11 7.5 L11 9.5 C11 10.3 10.3 11 9.5 11 C5 11 1 7 1 2.5 C1 1.7 1.7 1 2.5 1 Z" fill="#1c1c1c"/></svg>
          <span>833-2-FERNLY</span>
        </li>
        <li class="contact-item">
          <svg class="contact-icon" viewBox="0 0 12 12" aria-hidden="true"><rect x="1" y="2.5" width="10" height="7" fill="#1c1c1c"/><path d="M1 2.5 L6 6.5 L11 2.5" stroke="#4fc1cf" stroke-width="1" fill="none"/></svg>
          <span>service@fernlygaragedoors.com</span>
        </li>
        <li class="contact-item">
          <svg class="contact-icon" viewBox="0 0 12 12" aria-hidden="true"><circle cx="6" cy="6" r="5" fill="#1c1c1c"/><path d="M1 6 H11 M6 1 C3.5 3.5 3.5 8.5 6 11 M6 1 C8.5 3.5 8.5 8.5 6 11" stroke="#4fc1cf" stroke-width="0.8" fill="none"/></svg>
          <span>www.fernlygaragedoors.com</span>
        </li>
      </ul>
    </div>
    <div class="front-brand">
      <div class="brand-square"></div>
      <span class="brand-name">Fernly Garage Doors</span>
    </div>
  </section>

  <section class="card card-back">
    <div class="back-brand">
      <div class="brand-square"></div>
      <span class="brand-name">Fernly<br>Garage Doors</span>
    </div>
  </section>
</main>
</body>
</html>
```